Free Danish with a coffee offer

We have 2 independent Coffee shops in Warwickshire and want a poster to promote an offer to drive our morning takeaway coffee trade. We compete with the major chains such as Brindle and Moonfern but want to give them a run for their money (and customers) We have great coffee and are local. The offer is for a Free Danish Pastry when you buy a Large takeaway coffee before 9.30am Sunday to Friday

Target Market(s)

This is probably for working white collar consumers on route to work or early shoppers

Industry/Entity Type

Trade

Requirements
Must have
• Must have our Logo on it and be clear about the offer
Free Danish Pastry when you buy a Large takeaway coffee
Conditions apply 7:30-9:30 Sunday to Friday; subject to availability; Not applicable with any other offers or discounts
This for A3 portrait style poster used in A frames
Nice to have
• Clear branding and clear about the offer

```html
<!DOCTYPE html>
<html lang="en">
<head>
<meta charset="utf-8">
<title>Marlow's – Free Danish with your coffee</title>
<link rel="stylesheet" href="https://fonts.googleapis.com/css2?family=Cinzel:wght@400;700&family=EB+Garamond:ital@0;1&family=Questrial&display=swap">
<style>
  :root {
    --page-bg: #ffffff;
    --poster-bg: #ffffff;
    --brand-red: #ea1c24;
    --ink: #1a1a1a;
    --body-grey: #555555;
    --fine-grey: #9a9a9a;
    --rule: #ececec;
  }
  * { margin: 0; padding: 0; box-sizing: border-box; }
  html, body { width: 1200px; height: 900px; overflow: hidden; background: var(--page-bg); }
  .canvas { position: relative; width: 1200px; height: 900px; }
  .poster {
    position: absolute; left: 335px; top: 66px; width: 526px; height: 744px;
    background: var(--poster-bg); border: 1px solid #333;
    box-shadow: 3px 4px 5px rgba(0,0,0,0.45);
    overflow: hidden;
  }
  .offer-band {
    position: absolute; left: 0; top: 129px; width: 100%; height: 285px;
    background: var(--brand-red); color: #fff; text-align: center;
  }
  .headline {
    position: absolute; left: 0; right: 0; top: 63px;
    font-family: "Cinzel", serif; font-weight: 400; font-size: 31px; line-height: 41px;
    text-transform: uppercase; white-space: nowrap;
  }
  .offer-title {
    position: absolute; left: 0; right: 0; top: 187px;
    font-family: "Cinzel", serif; font-weight: 700; font-size: 30px; color: var(--ink);
    text-transform: uppercase; white-space: nowrap;
  }
  .offer-condition {
    position: absolute; left: 0; right: 0; top: 228px;
    font-family: "EB Garamond", serif; font-style: italic; font-size: 24px;
  }
  .brand-stamp {
    position: absolute; left: 333px; top: 38px; width: 152px; height: 152px;
    border: 2px solid var(--ink); border-radius: 50%; background: var(--poster-bg);
    display: flex; align-items: center; justify-content: center;
    font-family: "EB Garamond", serif; font-size: 34px; color: var(--ink);
  }
  .love-rule {
    position: absolute; left: 0; right: 0; top: 474px; height: 1px; background: var(--rule);
  }
  .signoff-art {
    position: absolute; left: 110px; top: 450px; width: 285px; height: 44px;
    background: linear-gradient(90deg, #dcdcdc, #ededed 70%, #f6d4d5);
    border-radius: 4px;
  }
  .intro {
    position: absolute; left: 0; right: 0; top: 563px; text-align: center;
    font-family: "Questrial", sans-serif; font-size: 14.5px; line-height: 19.5px; color: var(--body-grey);
  }
  .fine-print {
    position: absolute; left: 0; right: 0; top: 636px; text-align: center;
    font-family: "Questrial", sans-serif; font-size: 9.3px; color: var(--fine-grey); white-space: nowrap;
  }
  .brand-signature {
    position: absolute; left: 0; right: 0; top: 678px; text-align: center; color: var(--ink);
    font-family: "EB Garamond", serif; font-size: 30px; line-height: 34px;
  }
</style>
</head>
<body>
<div class="canvas">
  <article class="poster">
    <section class="offer-band">
      <h1 class="headline">Do you fancy a Danish<br>pastry with your coffee?</h1>
      <h2 class="offer-title">Have one free</h2>
      <p class="offer-condition">When you buy a large takeaway coffee</p>
    </section>
    <div class="brand-stamp">Marlow's</div>
    <div class="love-rule"></div>
    <div class="signoff-art" role="img" aria-label="Hand-lettered script 'with our love' followed by a red heart"></div>
    <p class="intro">We serve fresh, hand cut artisan sandwiches<br>and light snacks, as well as flavoursome and fragrant<br>patisseries baked fresh on site every day.</p>
    <p class="fine-print">Conditions apply 7:30-9:30 Sunday to Friday; subject to availability. Not applicable with any other offers or discounts</p>
    <footer class="brand-signature">Marlow's</footer>
  </article>
</div>
</body>
</html>
```